Business Card for Web Design consulting firm

Business card designs for Web Design consulting firm

Target Market(s)

English speaking adults ages 30 - 60. Predominantly professional services eg. Doctor, Dentist

Industry/Entity Type

Consulting

Requirements
Must have
• Double sided card

```html
<!DOCTYPE html>
<html lang="en">
<head>
<meta charset="utf-8">
<title>Korvane Business Card</title>
<link href="https://fonts.googleapis.com/css2?family=Noto+Sans:wght@400;700&family=Arimo&display=swap" rel="stylesheet">
<style>
  :root {
    --orange: #f7941d;
    --orange-light: #fbb04a;
    --ink: #4a4a4a;
    --black: #000000;
    --white: #ffffff;
    --card-back: #f1f1f1;
    --toolbar: #dcdcdc;
    --field-border: #9a9a9a;
  }
  * { margin: 0; padding: 0; box-sizing: border-box; }
  html, body { width: 938px; height: 1200px; overflow: hidden; }
  body {
    position: relative;
    background: var(--black);
    font-family: "Noto Sans", sans-serif;
    color: var(--ink);
  }
  .side-label {
    position: absolute;
    left: 21px;
    font-family: "Arimo", sans-serif;
    font-size: 18px;
    color: var(--white);
    letter-spacing: 0.5px;
  }
  .side-label--front { top: 15px; }
  .side-label--back { top: 612px; }

  .card {
    position: absolute;
    left: 22px;
    width: 893px;
    overflow: hidden;
  }
  .card--front { top: 46px; height: 546px; background: var(--white); }
  .card--back { top: 646px; height: 544px; background: var(--card-back); }

  .title-bar {
    position: absolute; left: 0; top: 0; width: 100%; height: 27px;
    background: linear-gradient(var(--orange-light), var(--orange) 60%, #f28a10);
  }
  .title-bar__name {
    position: absolute; left: 12px; top: 4px;
    font-size: 15px; color: var(--white); letter-spacing: 2px;
  }
  .window-buttons {
    position: absolute; right: 6px; top: 3px;
    display: flex; gap: 4px;
  }
  .window-buttons span {
    width: 23px; height: 20px; border: 2px solid var(--white);
  }
  .toolbar {
    position: absolute; left: 0; top: 27px; width: 100%; height: 35px;
    background: linear-gradient(#f2f2f2, var(--toolbar));
    border-bottom: 1px solid #bdbdbd;
  }
  .toolbar__icons { position: absolute; left: 12px; top: 7px; }
  .field {
    position: absolute; top: 6px; height: 23px;
    background: var(--white);
    border: 2px solid var(--field-border);
    border-right-color: #e4e4e4; border-bottom-color: #e4e4e4;
    font-size: 13px; line-height: 19px; padding-left: 8px;
    font-family: "Arimo", sans-serif; color: #333;
  }
  .field--address { left: 144px; width: 476px; }
  .field--search { left: 663px; width: 213px; padding-left: 4px; }
  .toolbar__tick { position: absolute; left: 628px; top: 8px; }
  .toolbar__info { position: absolute; left: 870px; top: 6px; }

  .brand {
    position: absolute;
    display: flex; align-items: center; gap: 16px;
    font-weight: 700; color: var(--ink); letter-spacing: 4px;
    white-space: nowrap;
  }
  .brand__dot { border-radius: 50%; background: var(--orange); flex: none; }
  .brand--front { left: 44px; top: 152px; font-size: 62px; }
  .brand--front .brand__dot { width: 44px; height: 44px; }
  .brand--back { right: 60px; top: 380px; font-size: 52px; }
  .brand--back .brand__dot { width: 38px; height: 38px; }

  .person {
    position: absolute; right: 49px; top: 347px; text-align: right;
  }
  .person__name { font-size: 29px; color: var(--orange); letter-spacing: 1px; line-height: 36px; }
  .person__role { font-size: 21px; font-weight: 700; letter-spacing: 1px; line-height: 26px; }

  .contact {
    position: absolute; right: 49px; top: 432px; text-align: right;
    font-size: 22px; line-height: 25px; letter-spacing: 1px;
  }
  .contact__key { color: var(--orange); }

  .address {
    position: absolute; left: 48px; top: 457px;
    font-size: 22px; line-height: 25px; letter-spacing: 0.5px;
  }
  .address__web { color: var(--orange); letter-spacing: 1.5px; }
</style>
</head>
<body>
  <div class="side-label side-label--front">Front:</div>

  <section class="card card--front">
    <div class="title-bar">
      <span class="title-bar__name">KORVANE</span>
      <div class="window-buttons"><span></span><span></span><span></span></div>
    </div>
    <div class="toolbar">
      <svg class="toolbar__icons" width="120" height="22" viewBox="0 0 120 22" aria-hidden="true">
        <polygon points="10,3 2,11 10,19" fill="var(--orange)"/>
        <polygon points="30,3 38,11 30,19" fill="var(--orange)"/>
        <path d="M60 5 L72 17 M72 5 L60 17" stroke="var(--orange)" stroke-width="3"/>
        <path d="M94 4 Q88 11 94 18 M102 4 Q108 11 102 18" stroke="var(--orange)" stroke-width="3" fill="none"/>
      </svg>
      <div class="field field--address">http://www.korvane.com</div>
      <svg class="toolbar__tick" width="20" height="18" viewBox="0 0 20 18" aria-hidden="true">
        <path d="M2 9 L8 15 L18 3" stroke="var(--orange)" stroke-width="4" fill="none"/>
      </svg>
      <div class="field field--search">Daniel Hart</div>
      <svg class="toolbar__info" width="22" height="22" viewBox="0 0 22 22" aria-hidden="true">
        <circle cx="11" cy="11" r="9" fill="none" stroke="var(--orange)" stroke-width="2"/>
        <rect x="10" y="9" width="2.5" height="8" fill="var(--orange)"/>
        <circle cx="11.2" cy="6" r="1.5" fill="var(--orange)"/>
      </svg>
    </div>

    <div class="brand brand--front"><span class="brand__dot"></span>KORVANE</div>

    <div class="person">
      <div class="person__name">Daniel Hart</div>
      <div class="person__role">Sales Person</div>
    </div>

    <div class="contact">
      <div><span class="contact__key">P:</span> 07 5550 1234</div>
      <div><span class="contact__key">M:</span> 0400 555 019</div>
      <div><span class="contact__key">E:</span> hello@korvane.com</div>
    </div>

    <div class="address">
      <div>22 Sample Lane, Brisbane, 4000</div>
      <div class="address__web">www.korvane.com</div>
    </div>
  </section>

  <div class="side-label side-label--back">Back:</div>

  <section class="card card--back">
    <div class="brand brand--back"><span class="brand__dot"></span>KORVANE</div>
  </section>
</body>
</html>
```